Business Cards for our company

Hi there,

we have successfully designed a logo with ArtFlock and would like now to design our business cards. We would like to keep the colours and the look-and-feel of the logo. Please send in variations with two or three colours and one or two sides. I promise to respond to every single submission.

Many thanks and happy new year.

All the best,
Wilfried

Target Market(s)

B2B

Industry/Entity Type

Trade

Contact Information for Business Card

We have successfully designed a logo with ArtFlock and would like now to design our business cards. We would like to keep the colours and the look-and-feel of the logo. Please send in variations with two or three colours and one or two sides. I promise to respond to every single submission.

Font styles to use
Serif
Sans Serif
Script

Requirements
Must have
• These information should be on the business card, grouped as you suggest, and we think using small pictograms for mobile, email, etc is pretty helpful:
• Wilfried Tammler (first and second name)
• Geschäftsführer/ Managing Director (title)
• KoR Warenkontor GmbH (company name and legal form)
• Ostheimer Str. 18/3 (street and house number)
• 73312 Lindenau (zip code and town)
• +491709384562 (mobile)
• +4975229027341 (work)
• w.tammler@kor-warenkontor.example (email)
• www.kor-warenkontor.example (web)
Nice to have
• Spectacular and interesting layout and design. You look at it and think, wow, that's not the normal stuff.
• We think of ourselves as bridge-builders between businesses (international producers on the one hand, and retail chains on the other hand) and we translate, organise and manage projects where both partners are involved, but it's difficult for them to cooperate due to language barriers and different working cultures.
• This is why we have the n between the B's shaped as a bridge, and the green arc supports this idea. Maybe you could play with this idea...
Should not have
• the standard layout that everybody has

```html
<!DOCTYPE html>
<html lang="en">
<head>
<meta charset="utf-8">
<title>KoR Warenkontor – Business Card</title>
<link rel="stylesheet" href="https://fonts.googleapis.com/css2?family=Open+Sans:wght@400;700&family=Tinos&display=swap">
<style>
  :root {
    --green: #3cf00a;
    --ink: #3a3a3a;
    --brand-grey: #555555;
    --icon-dark: #2f2f2f;
    --paper: #ffffff;
  }
  * { margin: 0; padding: 0; box-sizing: border-box; }
  html, body { width: 1200px; height: 765px; overflow: hidden; background: var(--paper); }
  .card { position: relative; width: 1200px; height: 765px; background: var(--paper); font-family: "Open Sans", sans-serif; color: var(--ink); }
  .band { position: absolute; background: var(--green); }
  .band-top { left: 0; top: 0; width: 1200px; height: 37px; }
  .band-left { left: 0; top: 0; width: 40px; height: 744px; }
  .band-right { left: 1162px; top: 0; width: 38px; height: 726px; }
  .band-bottom { left: 582px; top: 726px; width: 618px; height: 39px; }
  .band-spine { left: 582px; top: 264px; width: 38px; height: 501px; }

  .brand { position: absolute; left: 96px; top: 166px; width: 448px; text-align: center; color: var(--brand-grey); font-weight: 700; }
  .brand-name { font-size: 200px; line-height: 210px; letter-spacing: 4px; }
  .brand-sub { font-size: 42px; line-height: 52px; letter-spacing: 4px; text-transform: uppercase; }

  .person-name { position: absolute; left: 140px; top: 470px; width: 362px; text-align: center; font-size: 34px; font-weight: 400; }
  .person-title { position: absolute; left: 144px; top: 594px; font-family: "Tinos", serif; font-size: 46px; color: var(--green); white-space: nowrap; }

  .icon { position: absolute; }
  .icon-role { left: 0; top: 582px; width: 106px; height: 80px; }
  .icon-phone { left: 546px; top: 212px; width: 106px; height: 76px; }
  .icon-mail { left: 554px; top: 358px; width: 104px; height: 76px; }
  .icon-web { left: 550px; top: 486px; width: 104px; height: 76px; }
  .icon-pin { left: 550px; top: 622px; width: 106px; height: 80px; }

  .contact { position: absolute; font-size: 25px; line-height: 36px; text-shadow: 1px 1px 1px rgba(0,0,0,0.18); white-space: nowrap; }
  .contact-phone { left: 660px; top: 220px; }
  .contact-mail { left: 668px; top: 376px; }
  .contact-web { left: 672px; top: 500px; }
  .contact-address { left: 684px; top: 622px; line-height: 35px; }
</style>
</head>
<body>
<main class="card">
  <div class="band band-top"></div>
  <div class="band band-left"></div>
  <div class="band band-right"></div>
  <div class="band band-bottom"></div>
  <div class="band band-spine"></div>

  <div class="brand">
    <div class="brand-name">KoR</div>
    <div class="brand-sub">Warenkontor</div>
  </div>

  <p class="person-name">Wilfried Tammler</p>

  <svg class="icon icon-role" viewBox="0 0 106 80" aria-hidden="true">
    <rect x="0" y="0" width="106" height="80" rx="34" fill="var(--icon-dark)"/>
    <circle cx="46" cy="24" r="10" fill="#fff"/>
    <path d="M24 66 Q26 40 46 38 Q66 40 68 66 Z" fill="#fff"/>
  </svg>
  <p class="person-title">Managing Director</p>

  <svg class="icon icon-phone" viewBox="0 0 106 76" aria-hidden="true">
    <rect x="0" y="0" width="106" height="76" rx="32" fill="var(--icon-dark)"/>
    <rect x="42" y="16" width="22" height="42" rx="4" fill="none" stroke="#fff" stroke-width="3"/>
    <rect x="47" y="22" width="12" height="14" fill="#fff"/>
    <line x1="60" y1="16" x2="60" y2="8" stroke="#fff" stroke-width="3"/>
  </svg>
  <div class="contact contact-phone">+491709384562&nbsp;&nbsp;&nbsp;(mobile)<br>+4975229027341 (official)</div>

  <svg class="icon icon-mail" viewBox="0 0 104 76" aria-hidden="true">
    <rect x="0" y="0" width="104" height="76" rx="32" fill="var(--icon-dark)"/>
    <rect x="24" y="18" width="56" height="38" rx="3" fill="#fff"/>
    <path d="M24 20 L52 42 L80 20" fill="none" stroke="var(--icon-dark)" stroke-width="4"/>
  </svg>
  <div class="contact contact-mail">w.tammler@kor-warenkontor.example</div>

  <svg class="icon icon-web" viewBox="0 0 104 76" aria-hidden="true">
    <rect x="0" y="0" width="104" height="76" rx="32" fill="var(--icon-dark)"/>
    <circle cx="52" cy="38" r="24" fill="none" stroke="#fff" stroke-width="3"/>
    <ellipse cx="52" cy="38" rx="11" ry="24" fill="none" stroke="#fff" stroke-width="3"/>
    <line x1="28" y1="38" x2="76" y2="38" stroke="#fff" stroke-width="3"/>
  </svg>
  <div class="contact contact-web">www.kor-warenkontor.example</div>

  <svg class="icon icon-pin" viewBox="0 0 106 80" aria-hidden="true">
    <rect x="0" y="0" width="106" height="80" rx="34" fill="var(--icon-dark)"/>
    <path d="M53 12 a14 14 0 0 1 14 14 c0 10 -14 24 -14 24 c0 0 -14 -14 -14 -24 a14 14 0 0 1 14 -14 Z" fill="none" stroke="#fff" stroke-width="3"/>
    <circle cx="53" cy="26" r="5" fill="#fff"/>
    <path d="M30 56 L44 50 L62 56 L76 50 L80 68 L64 74 L44 68 L28 74 Z" fill="none" stroke="#fff" stroke-width="3"/>
  </svg>
  <div class="contact contact-address">KoR Warenkontor GmbH<br>Ostheimer Str. 18/3<br>73312 Lindenau</div>
</main>
</body>
</html>
```